Business Card design with fresh logo. Logo will also be used on website &, stationary etc

Target Market(s)

Corporate/Employers- The business is essentially in Wellness in the workplace or helping corporates contribute to employee wellbeing in many areas of their life both in the workplace and out with a view of improving performance, productivity, rentention etc. Given it''s nature the business is positioned as developing the employer brand ( language that is much more common within Australia) with many business''s desire to become Employer''s of Choice. As such I have settled on the trading name of ''Quorvalitude'' with a potential tag line ''Expand your employer brand!''

The following definition of Employer Brand from Zentrafolio captures the product positioning with a focus on internal stakeholders.

Pellowbrake (2005) defines your employer brand as “the image of your organization as a ‘great place to work’ in the minds of current employees and key stakeholders in the external market (active and passive candidates, clients, customers and other key stakeholders).”

Employer branding is therefore concerned with the attraction, engagement and retention initiatives targeted at enhancing a company''s employer brand.

Strong employer brands have employer value propositions ("EVPs") which are communicated in company actions and behaviours and evoke both emotive (e.g. I feel good about working here) and tangible benefits (this organisation cares about my career development) for current and prospective employees. These EVPs reflect the image that the organisations wants to portray to its target audience. A company’s employer brand is reflected in the actions and behaviours of leaders and is affected by company policies, procedures, and practices.

In today''s tight labor market it is essential that employers invest significant resources in their ''employer brand'' and increase their ''quorvalitude''

Requirements
Must have
• Name of Company ""Quorvalitude""

Business Card must be Horizontal
 
space for the tag line.. ""expand your employer brand"" but not necessary so flexibility to use it or not

```html
<!DOCTYPE html>
<html lang="en">
<head>
<meta charset="utf-8">
<title>Quorvalitude – Logo &amp; Business Card</title>
<link rel="stylesheet" href="https://fonts.googleapis.com/css2?family=Oswald:wght@500&family=Questrial&display=swap">
<style>
  :root {
    --paper: #ffffff;
    --card: #262220;
    --brand-orange: #f5a623;
    --ink: #231f1e;
    --black: #000000;
    --light-text: #d9d6d3;
  }
  * { margin: 0; padding: 0; box-sizing: border-box; }
  html, body { width: 1200px; height: 1000px; overflow: hidden; background: var(--paper); }
  .sheet { position: relative; width: 1200px; height: 1000px; }

  .wordmark {
    position: absolute;
    display: flex;
    align-items: center;
    gap: 12px;
    font-family: "Oswald", sans-serif;
    font-weight: 500;
    letter-spacing: 0.5px;
    line-height: 1;
  }
  .wordmark .dot { border-radius: 50%; flex: none; }

  .logo-colour { left: 63px; top: 118px; font-size: 40px; color: var(--ink); }
  .logo-colour .dot { width: 40px; height: 40px; background: var(--brand-orange); }

  .logo-mono { left: 63px; top: 266px; font-size: 40px; color: var(--black); }
  .logo-mono .dot { width: 40px; height: 40px; border: 7px solid var(--black); }

  .card {
    position: absolute;
    width: 723px;
    height: 442px;
    background: var(--card);
  }
  .card-front { left: 458px; top: 44px; }
  .card-back { left: 459px; top: 521px; }

  .card-front .wordmark {
    left: 0; right: 0; top: 196px;
    justify-content: center;
    font-size: 74px;
    color: var(--brand-orange);
    gap: 18px;
  }
  .card-front .dot { width: 70px; height: 70px; border: 12px solid var(--brand-orange); }

  .card-back .wordmark {
    left: 44px; top: 96px;
    font-size: 40px;
    color: var(--brand-orange);
  }
  .card-back .dot { width: 38px; height: 38px; border: 7px solid var(--brand-orange); }

  .contact {
    position: absolute;
    right: 41px;
    top: 150px;
    text-align: right;
    font-family: "Questrial", sans-serif;
    font-size: 25px;
    line-height: 29px;
    color: var(--light-text);
  }
  .contact p { white-space: nowrap; }
  .contact .group + .group { margin-top: 20px; }
  .contact .label { color: var(--brand-orange); }
  .contact .numbers p { line-height: 34px; }
</style>
</head>
<body>
<div class="sheet">
  <div class="wordmark logo-colour"><span class="dot"></span><span>QUORVALITUDE</span></div>
  <div class="wordmark logo-mono"><span class="dot"></span><span>QUORVALITUDE</span></div>

  <section class="card card-front">
    <div class="wordmark"><span class="dot"></span><span>QUORVALITUDE</span></div>
  </section>

  <section class="card card-back">
    <div class="wordmark"><span class="dot"></span><span>QUORVALITUDE</span></div>
    <div class="contact">
      <div class="group">
        <p>Marla Venn</p>
        <p>Managing Director</p>
      </div>
      <div class="group numbers">
        <p><span class="label">M</span> - 0412 708 219</p>
        <p><span class="label">E</span> - marla@quorvalitude.com.au</p>
        <p><span class="label">P</span> - 1800 604 372</p>
      </div>
      <div class="group">
        <p>48 Fenwick Lane Sydney NSW 2000</p>
        <p>Australia</p>
      </div>
    </div>
  </section>
</div>
</body>
</html>
```